Business Card Design Project

I have a two letter domain name qo.com.au (lower case font please). I want a business card, cum logo that is die cut (around the qo segment at least) that fits standard business card size.
qo is all about what 'I am' - a journalist, blogger, analyst, commentator. My mantra is "I wander so qo'.
The reverse of the card only needs my name Lon Fitch, email lon@qo.com.au and mobile +61 400 555 817
Target Market(s)
Mainly people that will use my professional writing services and suppliers that will provide product for review
Industry/Entity Type
Business
Requirements
Must have
- One side is qo.com.au (hint - the .com.au can be vertical or horizontal to fit - the qo should be as large as possible).
The other requires large size font name, email and phone details (so no one needs glasses to read it).
The die cut can be just to highlight the qo segment - need not be around the whole card.
Font used in the past was Belwe (old style - very much like the i used in the information symbol).
Colours - no preference - prefer two colour to process colour but can also be an outline font instead of solid colour.

```html
<!DOCTYPE html>
<html lang="en">
<head>
<meta charset="utf-8">
<title>qo.com.au business card</title>
<link rel="stylesheet" href="https://fonts.googleapis.com/css2?family=Jost:wght@400&display=swap">
<style>
  :root {
    --backdrop: #dcdcd8;
    --card: #ffffff;
    --brand-red: #e30613;
    --ink: #1a1a1a;
    --muted: #8a8a8a;
  }
  * { box-sizing: border-box; margin: 0; padding: 0; }
  html, body {
    width: 1200px;
    height: 1000px;
    overflow: hidden;
    background: var(--backdrop);
    font-family: "Jost", "Futura", sans-serif;
  }
  .canvas {
    position: relative;
    width: 1200px;
    height: 1000px;
  }
  .card {
    position: absolute;
    width: 560px;
    height: 340px;
    background: var(--card);
    box-shadow: 0 6px 18px rgba(0, 0, 0, 0.18);
    display: flex;
    align-items: center;
  }
  .card--front {
    left: 190px;
    top: 110px;
    padding-left: 90px;
    gap: 30px;
  }
  .card--back {
    left: 450px;
    top: 530px;
    justify-content: flex-end;
    padding-right: 80px;
    gap: 36px;
  }
  .brand-name {
    font-weight: 400;
    font-size: 96px;
    line-height: 1;
    color: var(--brand-red);
  }
  .identity__domain {
    font-size: 27px;
    font-weight: 400;
    color: var(--ink);
    line-height: 1.05;
  }
  .identity__tagline {
    font-size: 20px;
    font-weight: 400;
    color: var(--muted);
    line-height: 1.1;
  }
  .contact {
    font-style: normal;
    text-align: right;
    color: var(--brand-red);
    font-size: 19px;
    line-height: 1.15;
    font-weight: 400;
  }
</style>
</head>
<body>
  <main class="canvas">
    <section class="card card--front" aria-label="Card front">
      <p class="brand-name">qo</p>
      <div class="identity">
        <p class="identity__domain">qo.com.au</p>
        <p class="identity__tagline">I wander so qo'</p>
      </div>
    </section>

    <section class="card card--back" aria-label="Card back">
      <address class="contact">
        <p class="contact__name">Lon Fitch</p>
        <p class="contact__email">lon@qo.com.au</p>
        <p class="contact__phone">+61 400 555 817</p>
      </address>
      <p class="brand-name">qo</p>
    </section>
  </main>
</body>
</html>
```